Logo / Etikettendesign
Zielgruppe
Renommierte Sektkellerei will neue Wege gehen. Es wird ein neues Produkt kreirt - ein Sekt - der nicht als Sekt wahrgenommen werden soll - sondern als "Lifestyle" Produkt.
Der neue Name des Produktes steht fest "Wolkentanz"
Aufgabenstellung
Für den Namen "Wolkentanz" wird ein neues Logo / Schriftzug / Wortbildmarke gesucht, das gleich auf einem Etikett platziert werden soll.
Es kann Perlmutt sein, Es kann bunt sein. schön wäre (nicht unbedingt erforderlich) wenn ein Kussmund dabei wäre. Aber bitte nicht an dem Mund aufhängen. Es kann auch gerne in die Nostalgische Ebene übergehen.
Die Flasche wird dunkelgrün sein.
Es soll später noch ein Rosé in transparenter Flasche dazu kommen.

```html
<!DOCTYPE html>
<html lang="de">
<head>
<meta charset="utf-8">
<title>Wolkentanz – Jahrgangssekt Etikett</title>
<link rel="stylesheet" href="https://fonts.googleapis.com/css2?family=Cormorant+Garamond:wght@500;600&family=Libre+Caslon+Text&display=swap">
<style>
  :root {
    --stage: #2a2a2c;
    --label-black: #0e0e0f;
    --label-edge: #050505;
    --gold-light: #f6e2cf;
    --gold-mid: #d9b596;
    --gold-deep: #a8805f;
    --champagne: #efd8c4;
    --cream: #f7ede3;
    --ink-soft: #9a9a9a;
  }
  html, body {
    margin: 0;
    width: 1200px;
    height: 1200px;
    overflow: hidden;
    background: var(--stage);
  }
  .label-canvas {
    display: block;
    width: 1200px;
    height: 1200px;
    background: radial-gradient(circle at 60% 30%, #3a3a3c 0%, var(--stage) 70%);
  }
  .brand-name {
    font-family: "Cormorant Garamond", "Times New Roman", serif;
    font-weight: 600;
    font-size: 84px;
    letter-spacing: 1px;
  }
  .category {
    font-family: "Libre Caslon Text", Georgia, serif;
    font-size: 17px;
    letter-spacing: 1.5px;
    fill: var(--ink-soft);
  }
  .taste {
    font-family: "Libre Caslon Text", Georgia, serif;
    font-size: 30px;
    fill: #3a2a20;
  }
</style>
</head>
<body>
<svg class="label-canvas" viewBox="0 0 1200 1200" xmlns="http://www.w3.org/2000/svg">
  <defs>
    <path id="shield" d="M190,250 C260,165 520,150 600,212 C680,150 940,165 1010,250 C1020,400 1010,520 1005,640 C1000,880 800,1030 600,1062 C400,1030 200,880 195,640 C190,520 180,400 190,250 Z"/>
    <linearGradient id="goldFoil" x1="0" y1="0" x2="1" y2="1">
      <stop offset="0" stop-color="var(--gold-light)"/>
      <stop offset="0.5" stop-color="var(--gold-deep)"/>
      <stop offset="1" stop-color="var(--gold-light)"/>
    </linearGradient>
    <linearGradient id="titleFoil" x1="0" y1="0" x2="0" y2="1">
      <stop offset="0" stop-color="#fff4ea"/>
      <stop offset="0.55" stop-color="var(--champagne)"/>
      <stop offset="1" stop-color="var(--gold-mid)"/>
    </linearGradient>
    <linearGradient id="bandFill" x1="0" y1="0" x2="1" y2="0">
      <stop offset="0" stop-color="var(--gold-mid)"/>
      <stop offset="0.5" stop-color="var(--cream)"/>
      <stop offset="1" stop-color="var(--gold-mid)"/>
    </linearGradient>
    <radialGradient id="bubbleGlow" cx="0.5" cy="0.45" r="0.55">
      <stop offset="0" stop-color="var(--champagne)" stop-opacity="0.85"/>
      <stop offset="1" stop-color="var(--gold-deep)" stop-opacity="0.15"/>
    </radialGradient>
    <radialGradient id="flourishGlow" cx="0.5" cy="0.5" r="0.5">
      <stop offset="0" stop-color="var(--gold-mid)" stop-opacity="0.55"/>
      <stop offset="1" stop-color="var(--gold-mid)" stop-opacity="0"/>
    </radialGradient>
    <clipPath id="innerClip">
      <use href="#shield" transform="translate(600 606) scale(0.9) translate(-600 -606)"/>
    </clipPath>
  </defs>

  <g class="label">
    <use href="#shield" fill="var(--label-edge)" stroke="var(--label-edge)" stroke-width="16"/>
    <use class="foil-frame" href="#shield" fill="url(#goldFoil)" transform="translate(600 606) scale(0.965) translate(-600 -606)"/>
    <use href="#shield" fill="var(--label-edge)" transform="translate(600 606) scale(0.93) translate(-600 -606)"/>
    <use class="label-field" href="#shield" fill="var(--label-black)" stroke="var(--gold-mid)" stroke-width="2" transform="translate(600 606) scale(0.9) translate(-600 -606)"/>

    <g role="img" aria-label="Kussmund aus Champagnerperlen mit aufsteigenden Perlen">
      <ellipse cx="600" cy="320" rx="170" ry="95" fill="url(#bubbleGlow)"/>
      <ellipse cx="600" cy="435" rx="22" ry="50" fill="url(#bubbleGlow)" opacity="0.6"/>
    </g>

    <text class="brand-name" x="600" y="600" text-anchor="middle" textLength="560" lengthAdjust="spacingAndGlyphs" fill="url(#titleFoil)">WOLKENTANZ</text>

    <line x1="352" y1="651" x2="508" y2="651" stroke="var(--ink-soft)" stroke-width="1.5"/>
    <line x1="692" y1="651" x2="848" y2="651" stroke="var(--ink-soft)" stroke-width="1.5"/>
    <text class="category" x="600" y="657" text-anchor="middle">Jahrgangssekt</text>

    <ellipse role="img" aria-label="Verschnörkeltes Ornament" cx="600" cy="795" rx="140" ry="50" fill="url(#flourishGlow)"/>

    <g clip-path="url(#innerClip)">
      <path d="M180,880 C380,870 500,845 600,845 C700,845 820,870 1020,880 L1020,1100 L180,1100 Z" fill="url(#bandFill)"/>
    </g>
    <text class="taste" x="600" y="945" text-anchor="middle">trocken</text>
  </g>
</svg>
</body>
</html>
```